Business Card Design

Please visit www.MarkDorsey.com to acquire information for business card.

Back Side of Card:
a lifetime of experience working for you.

With over 25 years in the construction industry, well over a decade as a licensed Subcontractor / General Contractor and nearly 10 years as a licensed Realtor, I have excelled and cultivated a working knowledge of how all the pieces fit together.

Here is a link to folder.
https://files.examplecloud.net/folderview?id=7Qk2mXrTpLw9zVbN4sHcDyUeFaGj&usp=sharing

Industry/Entity Type

Construction

Contact Information for Business Card

Company: Mark Dorsey, LLC.
Address: 31872 W. Cedar Hollow Blvd. Suite 207-418
Name: Mark Dorsey
Phone: (623) 587-2914
Web: www.MarkDorsey.com
Type of services offered: Architectural Design, 3D Models, Renderings & Animation - Construction Documents - Project Managment.

```html
<!DOCTYPE html>
<html lang="en">
<head>
<meta charset="utf-8">
<title>Mark Dorsey, LLC. — Business Card</title>
<link rel="stylesheet" href="https://fonts.googleapis.com/css2?family=Saira+Condensed:wght@400;500&family=Saira+Semi+Condensed:wght@400&family=Saira:wght@400&display=swap">
<style>
  :root {
    --stage: #6f6f6f;
    --card-dark: #232323;
    --card-mid: #3a3a3a;
    --text-light: #f2f2f2;
    --text-muted: #9a9a9a;
    --band-light: #d9d9d9;
    --band-dark: #a9a9a9;
    --name-ink: #3a3a3a;
    --rule: #8a8a8a;
  }
  * { margin: 0; padding: 0; box-sizing: border-box; }
  html, body { width: 1200px; height: 1000px; overflow: hidden; }
  body {
    background: var(--stage);
    position: relative;
    font-family: "Saira Condensed", "Arial Narrow", sans-serif;
  }
  .card {
    position: absolute;
    left: 286px;
    width: 628px;
    height: 358px;
    overflow: hidden;
    background: var(--card-dark);
    box-shadow: 0 6px 18px rgba(0,0,0,.35);
  }
  .card--back { top: 100px; }
  .card--front { top: 542px; }
  .card__backdrop {
    position: absolute; inset: 0;
    background: linear-gradient(135deg, #3d3d3d 0%, #2a2a2a 45%, #1e1e1e 70%, #333 100%);
  }
  .back__content {
    position: absolute; left: 42px; right: 36px; top: 34px;
    color: var(--text-light);
  }
  .back__headline {
    font-family: "Saira Condensed", "Arial Narrow", sans-serif;
    font-weight: 500;
    font-size: 25px;
    text-align: right;
    letter-spacing: .3px;
    margin-bottom: 18px;
  }
  .back__story {
    font-family: "Saira Semi Condensed", "Arial Narrow", sans-serif;
    font-size: 21px;
    line-height: 1.4;
  }
  .brand {
    position: absolute; left: 37px; top: 34px;
    display: flex; align-items: center; gap: 22px;
  }
  .brand__square {
    width: 100px; height: 88px;
    border: 2px solid var(--rule);
  }
  .brand__name {
    font-size: 38px; color: var(--text-muted); font-weight: 400;
  }
  .name-band {
    position: absolute; left: 0; top: 143px; width: 628px; height: 38px;
    background: linear-gradient(90deg, var(--band-dark), var(--band-light) 60%, #ececec);
  }
  .name-band__name {
    position: absolute; left: 58px; top: 0;
    font-family: "Saira", "Arial", sans-serif;
    font-size: 29px; line-height: 38px; letter-spacing: 1.5px;
    color: var(--name-ink);
  }
  .contact {
    position: absolute; left: 38px; top: 190px;
    border-left: 2px solid var(--rule);
    padding-left: 14px;
    color: var(--text-light);
    font-size: 18px; line-height: 23px;
    list-style: none;
  }
  .contact__item { display: flex; align-items: center; gap: 10px; }
  .contact__icon { width: 20px; height: 18px; flex: none; }
  .services {
    position: absolute; left: 0; right: 0; top: 262px;
    text-align: center; color: var(--text-light);
  }
  .services__title {
    font-size: 18px; text-decoration: underline; text-underline-offset: 3px;
    margin-bottom: 6px; margin-left: 0;
  }
  .services__list { font-size: 16px; line-height: 19px; }
</style>
</head>
<body>

<section class="card card--back" aria-label="Card back">
  <div class="card__backdrop" role="img" aria-label="Dark faded photograph of roof framing overlaid with architectural plans"></div>
  <div class="back__content">
    <h2 class="back__headline">A LIFETIME OF EXPERIENCE WORKING FOR YOU.</h2>
    <p class="back__story">with over 25 years in the construction industry, well over a decade as a licensed Subcontractor/General contractor and nearly 10 years as a licensed Realtor, I have excelled and cultivated a working knowledge of how all the pieces fit together.</p>
  </div>
</section>

<section class="card card--front" aria-label="Card front">
  <div class="card__backdrop" role="img" aria-label="Dark faded photograph of a building frame overlaid with architectural plans"></div>

  <div class="brand">
    <div class="brand__square"></div>
    <span class="brand__name">Mark Dorsey, LLC.</span>
  </div>

  <div class="name-band"><span class="name-band__name">Mark Dorsey</span></div>

  <ul class="contact">
    <li class="contact__item">
      <svg class="contact__icon" viewBox="0 0 20 18" fill="none" stroke="#eee" stroke-width="1.6"><path d="M2 9 L10 2 L18 9"/><path d="M4 8 V16 H16 V8"/><rect x="8" y="11" width="4" height="5"/></svg>
      <span>31872 W. Cedar Hollow Blvd. Suite 207-418.</span>
    </li>
    <li class="contact__item">
      <svg class="contact__icon" viewBox="0 0 20 18"><rect x="1" y="0" width="18" height="18" rx="3" fill="#eee"/><path d="M6 4 C5 8 8 13 13 14 L14.5 12 L12 10.5 L11 11.5 C9.5 11 8 9 7.5 7.5 L8.5 6.5 L7.5 4 Z" fill="#232323"/></svg>
      <span>(623) 587-2914</span>
    </li>
    <li class="contact__item">
      <svg class="contact__icon" viewBox="0 0 20 18" fill="none" stroke="#eee" stroke-width="1.3"><circle cx="10" cy="9" r="7.5"/><ellipse cx="10" cy="9" rx="3.2" ry="7.5"/><path d="M2.5 9 H17.5 M4 5 H16 M4 13 H16"/></svg>
      <span>www.MarkDorsey.com</span>
    </li>
  </ul>

  <div class="services">
    <p class="services__title">Type of services offered</p>
    <p class="services__list">Architectural Design ♦ 3D Models ♦ Rendering &amp; Animation<br>Construction Documents ♦ Project Managements</p>
  </div>
</section>

</body>
</html>
```